Can You Help Sell Glass Cabinets with a Banner Ad?

Our New Zealand-based company designs and sells glass cabinets and display cases. 75% of our customers are other businesses who want to display products in their shop or showroom. The other 25% of our customers are householders who want a glass cabinet for their personal collectables. We have been trading 2 years now, and are expanding rapidly. Our website address is www.vitrinaplace.example.nz.
We have made a strategic decision to focus on online advertising this year. This is because we want to raise our profile to the greatest number of and widest range of people. For now, this means banner advertising on high traffic New Zealand-based websites in an attempt to generate more traffic to our website. The websites we will initially use are www.ploverpost.example.nz and www.tuidaily.example.nz.
We therefore need a set of eye-catching banner ads designed for our online marketing campaign. The three banners required will probably just be variations on a single design.

Banner 1: Top Banner
760x120

Banner 2: Skyscraper
160x600

Banner 3: Medium Rectangle
300x250

Target Market(s)

The primary target market will be retailers who have shops and showrooms. They may not yet know they need a showcase.

Industry/Entity Type

Advertising

Requirements
Must have
• Vitrina Place logo
"High quality glass cabinets and showcases"
Maybe also "Show your products, not the cabinet"
[Corporate colour is green, as per logo. Secondary colours are orange, purple and grey.]
[Please use New Zealand (British) spelling]

Nice to have
• Please view our website and brochure on the Resources page for the look and feel of our company. In particular we like our logo, so it is possible you can take a lead from this. The logo emblem is designed to be evocative of glass.
The logo spot colour is 41,0,70,10.

```html
<!DOCTYPE html>
<html lang="en-NZ">
<head>
<meta charset="utf-8">
<title>Vitrina Place – banner set</title>
<link rel="stylesheet" href="https://fonts.googleapis.com/css2?family=Source+Sans+3:wght@300;400;600&display=swap">
<style>
  :root {
    --board-light: #fbfcf4;
    --board-mid: #eef1dc;
    --board-edge: #d7dfb6;
    --plum: #4d2f4b;
    --plum-panel-top: #8a6d84;
    --plum-panel-bottom: #5b3e58;
    --leaf: #bccc8e;
    --leaf-pale: #dfe8c4;
    --frost: #f5f4ee;
    --mist: #e4dce3;
    --label-ink: #222222;
    --shadow: rgba(60, 50, 40, 0.35);
  }
  * { margin: 0; padding: 0; box-sizing: border-box; }
  html, body { width: 1096px; height: 1200px; overflow: hidden; }
  body {
    position: relative;
    font-family: "Source Sans 3", "Myriad Pro", sans-serif;
    font-weight: 300;
    background: radial-gradient(ellipse 620px 620px at 400px 420px, var(--board-light) 0%, var(--board-mid) 45%, var(--board-edge) 100%);
  }
  .banner {
    position: absolute;
    overflow: hidden;
    background: var(--plum);
    box-shadow: 2px 3px 6px var(--shadow);
  }
  .banner-top { left: 41px; top: 68px; width: 1011px; height: 159px; }
  .banner-rectangle { left: 110px; top: 529px; width: 399px; height: 332px; }
  .banner-skyscraper { left: 724px; top: 300px; width: 213px; height: 797px; }

  .brand-panel {
    position: absolute;
    background: linear-gradient(180deg, var(--plum-panel-top) 0%, var(--plum-panel-bottom) 100%);
    box-shadow: 0 0 6px rgba(0,0,0,0.35);
  }
  .brand-panel .sheen { position: absolute; inset: 0; width: 100%; height: 100%; }
  .banner-top .brand-panel { left: 563px; top: 0; width: 448px; height: 159px; }
  .banner-rectangle .brand-panel { left: 0; top: 246px; width: 399px; height: 86px; }
  .banner-skyscraper .brand-panel { left: 0; top: 0; width: 213px; height: 239px; }

  .line, .brand-name, .brand-tagline, .strapline, .label {
    position: absolute;
    line-height: 1;
    white-space: nowrap;
  }
  .line { color: var(--leaf); }
  .line .accent { color: var(--frost); }

  .brand-mark { position: absolute; background: var(--leaf-pale); opacity: 0.9; }
  .brand-name { color: var(--leaf); font-weight: 600; letter-spacing: 0.5px; }
  .brand-tagline { color: var(--leaf); font-weight: 400; }
  .strapline { color: var(--mist); font-weight: 400; }

  .centred { left: 0; width: 100%; text-align: center; }

  .label { color: var(--label-ink); font-size: 26px; font-weight: 400; }
</style>
</head>
<body>

  <!-- Top banner 760x120 -->
  <section class="banner banner-top" aria-label="Top banner">
    <p class="line" style="left:16px; top:10px; font-size:75px;">High quality <span class="accent">glass</span></p>
    <p class="line" style="left:16px; top:84px; font-size:55px;">cabinets and showcases</p>
    <div class="brand-panel">
      <svg class="sheen" viewBox="0 0 448 159" preserveAspectRatio="none" aria-hidden="true">
        <path d="M0 0 H448 V40 Q220 90 0 70 Z" fill="#ffffff" opacity="0.08"/>
      </svg>
      <div class="brand-mark" style="left:18px; top:22px; width:46px; height:46px;"></div>
      <p class="brand-name" style="left:78px; top:18px; font-size:36px;">VITRINA PLACE</p>
      <p class="brand-tagline" style="left:78px; top:56px; font-size:23px;">design strength value</p>
      <p class="strapline" style="left:20px; top:108px; font-size:27px;">Show your products, not the cabinet</p>
    </div>
  </section>
  <p class="label" style="left:41px; top:239px;">Banner 1: Top Banner</p>
  <p class="label" style="left:41px; top:274px;">760x120</p>

  <!-- Medium rectangle 300x250 -->
  <section class="banner banner-rectangle" aria-label="Medium rectangle banner">
    <p class="line" style="left:14px; top:16px; font-size:61px;">High quality</p>
    <p class="line" style="left:14px; top:88px; font-size:61px;"><span class="accent">glass</span> cabinets</p>
    <p class="line" style="left:14px; top:160px; font-size:61px;">and showcases</p>
    <div class="brand-panel">
      <svg class="sheen" viewBox="0 0 399 86" preserveAspectRatio="none" aria-hidden="true">
        <path d="M0 0 H399 V22 Q200 52 0 40 Z" fill="#ffffff" opacity="0.08"/>
      </svg>
      <div class="brand-mark" style="left:16px; top:18px; width:38px; height:38px;"></div>
      <p class="brand-name" style="left:64px; top:14px; font-size:32px;">VITRINA PLACE</p>
      <p class="brand-tagline" style="left:64px; top:52px; font-size:20px;">design strength value</p>
    </div>
  </section>
  <p class="label" style="left:110px; top:888px;">Banner 3: Medium Rectangle</p>
  <p class="label" style="left:110px; top:925px;">300x250</p>

  <!-- Skyscraper 160x600 -->
  <section class="banner banner-skyscraper" aria-label="Skyscraper banner">
    <div class="brand-panel">
      <svg class="sheen" viewBox="0 0 213 239" preserveAspectRatio="none" aria-hidden="true">
        <path d="M0 0 H213 V120 Q100 170 0 150 Z" fill="#ffffff" opacity="0.07"/>
      </svg>
      <div class="brand-mark" style="left:56px; top:36px; width:100px; height:100px;"></div>
      <p class="brand-name" style="left:6px; top:180px; font-size:28px;">VITRINA PLACE</p>
      <p class="brand-tagline" style="left:6px; top:212px; font-size:15px;">design strength value</p>
    </div>
    <p class="line centred" style="top:275px; font-size:82px;">High</p>
    <p class="line centred" style="top:385px; font-size:58px;">quality</p>
    <p class="line centred" style="top:458px; font-size:82px;"><span class="accent">glass</span></p>
    <p class="line centred" style="top:555px; font-size:53px;">cabinets</p>
    <p class="line centred" style="top:620px; font-size:106px;">and</p>
    <p class="line centred" style="top:728px; font-size:40px;">showcases</p>
  </section>
  <p class="label" style="left:724px; top:1122px;">Banner 2: Skyscraper</p>
  <p class="label" style="left:724px; top:1156px;">160x600</p>

</body>
</html>
```